Software Development Consulting Company Needs Business Card Design

We need a new business card design for our consultants at Marendo Solutions (marendosolutions.example). We are a small firm that provides high-end software development and methodology consulting to medium to large enterprise IT organizations.

Our logo uses Futura for the font and we would like to stick with navy blue and canary yellow for the logo colors. Attached are normal and reversed versions of our logos in illustrator format.
Updates

Hi Everyone, Thank yo very much for your amazing design ideas. I have created a poll for this project and our employees will be voting on the design they wish to use. We will be making a decision this Wednesday (October 22nd). Thanks again, Gavin Hartwell

Industry/Entity Type

Business

```html
<!DOCTYPE html>
<html lang="en">
<head>
<meta charset="utf-8">
<title>Marendo Solutions – Business Card</title>
<link rel="stylesheet" href="https://fonts.googleapis.com/css2?family=Jost:wght@400;500;600&display=swap">
<style>
  :root {
    --stage: #2b2b2b;
    --card-black: #050505;
    --card-black-soft: #1a1a1a;
    --navy: #1f4674;
    --navy-light: #2f66a6;
    --navy-deep: #15294a;
    --canary: #f2e200;
    --canary-dim: #b8a838;
    --white: #f4f4f4;
  }
  * { margin: 0; padding: 0; box-sizing: border-box; }
  html, body {
    width: 1200px;
    height: 1028px;
    overflow: hidden;
    background: var(--stage);
    font-family: "Jost", "Futura", sans-serif;
  }
  .sheet {
    position: relative;
    width: 1200px;
    height: 1028px;
    display: flex;
    align-items: center;
    justify-content: center;
    gap: 40px;
  }
  .card {
    position: relative;
    width: 560px;
    height: 320px;
    overflow: hidden;
    box-shadow: 0 14px 30px rgba(0,0,0,0.55);
  }

  /* Front: contact side */
  .card-front {
    background: radial-gradient(ellipse at 45% 40%, var(--card-black-soft) 0%, var(--card-black) 70%);
  }
  .top-tab {
    position: absolute;
    top: 0;
    right: 0;
    width: 150px;
    height: 10px;
    background: var(--navy);
  }
  .name-row {
    position: absolute;
    left: 0;
    top: 112px;
    width: 100%;
    height: 66px;
  }
  .chevrons-left {
    position: absolute;
    left: 18px;
    top: 8px;
  }
  .person-name {
    position: absolute;
    left: 90px;
    top: 14px;
    color: var(--white);
    font-size: 24px;
    font-weight: 400;
    letter-spacing: 2px;
    line-height: 1;
    white-space: nowrap;
  }
  .chevrons-right {
    position: absolute;
    left: 232px;
    top: 8px;
  }
  .logo-band {
    position: absolute;
    left: 312px;
    top: 0;
    right: 0;
    height: 66px;
    background: linear-gradient(90deg, var(--navy) 0%, var(--navy-light) 100%);
    display: flex;
    align-items: center;
    padding: 0 12px 0 14px;
    gap: 8px;
  }
  .brand-dot {
    width: 8px;
    height: 8px;
    border-radius: 50%;
    background: var(--canary);
    flex: none;
  }
  .brand-name {
    color: var(--white);
    font-weight: 400;
    text-transform: uppercase;
    white-space: nowrap;
    line-height: 1;
  }
  .logo-band .brand-name {
    font-size: 15px;
    letter-spacing: 2px;
  }
  .contact-list {
    position: absolute;
    left: 22px;
    top: 206px;
    list-style: none;
    display: flex;
    flex-direction: column;
    gap: 10px;
  }
  .contact-item {
    display: flex;
    align-items: center;
    gap: 12px;
    color: var(--canary);
    font-size: 15px;
    font-weight: 600;
    letter-spacing: 1.5px;
  }
  .contact-icon {
    width: 22px;
    height: 22px;
    background: var(--navy);
    display: flex;
    align-items: center;
    justify-content: center;
  }

  /* Back: brand side */
  .card-back {
    background: radial-gradient(ellipse at 50% 45%, var(--navy-light) 0%, var(--navy) 50%, var(--navy-deep) 100%);
    display: flex;
    align-items: center;
    justify-content: center;
    gap: 14px;
  }
  .card-back .brand-dot {
    width: 14px;
    height: 14px;
  }
  .card-back .brand-name {
    font-size: 34px;
    letter-spacing: 5px;
  }
</style>
</head>
<body>
<main class="sheet">

  <section class="card card-front" aria-label="Business card front">
    <div class="top-tab"></div>

    <div class="name-row">
      <svg class="chevrons-left" width="64" height="50" viewBox="0 0 64 50" aria-hidden="true">
        <polygon points="26,0 36,0 14,25 36,50 26,50 4,25" fill="var(--canary)"/>
        <polygon points="40,0 50,0 28,25 50,50 40,50 18,25" fill="var(--canary-dim)" opacity="0.8"/>
        <polygon points="54,0 64,0 42,25 64,50 54,50 32,25" fill="var(--canary-dim)" opacity="0.45"/>
      </svg>

      <p class="person-name">Your Name</p>

      <svg class="chevrons-right" width="64" height="50" viewBox="0 0 64 50" aria-hidden="true">
        <polygon points="0,0 10,0 32,25 10,50 0,50 22,25" fill="var(--canary-dim)" opacity="0.45"/>
        <polygon points="14,0 24,0 46,25 24,50 14,50 36,25" fill="var(--canary-dim)" opacity="0.8"/>
        <polygon points="28,0 38,0 60,25 38,50 28,50 50,25" fill="var(--canary)"/>
      </svg>

      <div class="logo-band">
        <span class="brand-dot"></span>
        <span class="brand-name">Marendo Solutions</span>
      </div>
    </div>

    <ul class="contact-list">
      <li class="contact-item">
        <span class="contact-icon">
          <svg width="14" height="14" viewBox="0 0 14 14" aria-hidden="true">
            <path d="M1 5 Q7 0 13 5 L11 7 L9 5.5 L5 5.5 L3 7 Z" fill="var(--canary)"/>
            <rect x="3" y="7" width="8" height="6" rx="1" fill="var(--canary)"/>
          </svg>
        </span>
        Phone Number
      </li>
      <li class="contact-item">
        <span class="contact-icon">
          <svg width="14" height="12" viewBox="0 0 14 12" aria-hidden="true">
            <rect x="0.5" y="1" width="13" height="10" fill="var(--canary)"/>
            <polyline points="0.5,1 7,7 13.5,1" fill="none" stroke="var(--navy)" stroke-width="1.2"/>
          </svg>
        </span>
        Email Addres
      </li>
      <li class="contact-item">
        <span class="contact-icon">
          <svg width="14" height="14" viewBox="0 0 14 14" aria-hidden="true">
            <g fill="none" stroke="var(--canary)" stroke-width="1">
              <circle cx="7" cy="7" r="6"/>
              <ellipse cx="7" cy="7" rx="2.6" ry="6"/>
              <line x1="1" y1="7" x2="13" y2="7"/>
            </g>
          </svg>
        </span>
        Website
      </li>
    </ul>
  </section>

  <section class="card card-back" aria-label="Business card back">
    <span class="brand-dot"></span>
    <span class="brand-name">Marendo Solutions</span>
  </section>

</main>
</body>
</html>
```